Voltra Enterprises, LLC

We are a design build general contracting company.
We work with commercial accounts and private developers. We build retail spaces, restaurants and housing projects.
Im looking for a clean professional type of logo incorporating a roman flavor, think ionic columns and pedestals.
Two toned colorway.
I like unusual fonts and Im not afraid to do something bold with the logo.
Contact Information for Business Card
Marnie Quellstrom
415-872-3190 voltramq@brevomail.example
Font styles to use
Decorative
Colors
Designer to choose colors to be used in the design.
Requirements
Should not have
- I don't like reds pinks.

```html
<!DOCTYPE html>
<html lang="en">
<head>
<meta charset="utf-8">
<title>Voltra Enterprises, LLC – Business Card</title>
<link rel="stylesheet" href="https://fonts.googleapis.com/css2?family=Montserrat:wght@600;700&family=Open+Sans:wght@400&display=swap">
<style>
  :root {
    --bg: #1f1f1f;
    --taupe: #8a8478;
    --taupe-dark: #5f5a51;
    --card-white: #ffffff;
    --ink: #111111;
    --ink-soft: #333333;
  }
  * { margin: 0; padding: 0; box-sizing: border-box; }
  html, body {
    width: 1200px;
    height: 900px;
    overflow: hidden;
    background: var(--bg);
  }
  .stage {
    position: relative;
    width: 1200px;
    height: 900px;
  }
  .card {
    position: absolute;
    width: 525px;
    height: 300px;
    border-radius: 30px;
    overflow: hidden;
  }
  .card--back {
    left: 80px;
    top: 110px;
    background: var(--taupe);
  }
  .card--front {
    left: 595px;
    top: 490px;
    background: var(--card-white);
  }
  .brand {
    position: absolute;
    display: flex;
    align-items: center;
    gap: 10px;
    font-family: "Montserrat", sans-serif;
    font-weight: 700;
    font-size: 17px;
    line-height: 1.3;
    letter-spacing: 0.04em;
    text-transform: uppercase;
    white-space: nowrap;
  }
  .brand__mark {
    width: 14px;
    height: 14px;
    flex: none;
  }
  .card--back .brand {
    left: 50%;
    top: 50%;
    transform: translate(-50%, -50%);
    color: var(--taupe-dark);
  }
  .card--back .brand__mark { background: var(--taupe-dark); }
  .card--front .brand {
    left: 52px;
    top: 50%;
    transform: translateY(-50%);
    font-size: 14px;
    color: var(--taupe);
  }
  .card--front .brand__mark { background: var(--taupe); }
  .contact {
    position: absolute;
    left: 285px;
    top: 100px;
  }
  .contact__name {
    font-family: "Montserrat", sans-serif;
    font-weight: 600;
    font-size: 20px;
    color: var(--ink);
    margin-bottom: 20px;
    white-space: nowrap;
  }
  .contact__line {
    display: flex;
    align-items: center;
    gap: 8px;
    font-family: "Open Sans", sans-serif;
    font-size: 13px;
    color: var(--ink-soft);
    margin-bottom: 10px;
    white-space: nowrap;
  }
  .contact__icon {
    width: 14px;
    height: 14px;
    fill: #666;
    flex: none;
  }
</style>
</head>
<body>
<main class="stage">
  <section class="card card--back" aria-label="Business card back">
    <div class="brand"><span class="brand__mark"></span>Voltra Enterprises, LLC</div>
  </section>

  <section class="card card--front" aria-label="Business card front">
    <div class="brand"><span class="brand__mark"></span><span>Voltra<br>Enterprises, LLC</span></div>
    <div class="contact">
      <p class="contact__name">Marnie Quellstrom</p>
      <p class="contact__line">
        <svg class="contact__icon" viewBox="0 0 16 16" aria-hidden="true">
          <path d="M1 6c0-2 3-3.5 7-3.5S15 4 15 6v1h-3.5V5.5h-7V7H1z"/>
          <rect x="3" y="8" width="10" height="6" rx="1.5"/>
        </svg>
        415-872-3190
      </p>
      <p class="contact__line">
        <svg class="contact__icon" viewBox="0 0 16 16" aria-hidden="true">
          <path d="M1 4h14v9H1z M1.5 4.5 8 9.5l6.5-5" stroke="#fff" stroke-width="0.8"/>
        </svg>
        voltramq@brevomail.example
      </p>
    </div>
  </section>
</main>
</body>
</html>
```